Pinecrest Valley Armory Banner

We are looking for a banner ad that we will run on DawnLedger.com the size is 758x120 and also a matching one that is 300x250 can be animated or static.final graphics will need to be submitted in jpg, gif or similar format. Our shop is a firearms business called "Pinecrest Valley Armory" located at 412 Route 19 South, Ridgeford Vy. 39417 phone is 555-574-3186 . it need to be modern and eye catching and be more geared to the tactical side. Our website is
pinecrestarmory.com the banners DO NOT have to match website. would like a DIFFERENT LOOK than my website

```html
<!DOCTYPE html>
<html lang="en">
<head>
<meta charset="utf-8">
<title>Pinecrest Valley Armory Banner</title>
<link rel="stylesheet" href="https://fonts.googleapis.com/css2?family=Open+Sans:wght@400;600;700&display=swap">
<style>
  :root {
    --bg-top: #ececec;
    --bg-bottom: #dcdcdc;
    --brand-red: #7d0a0a;
    --brand-brown: #3b2a1f;
    --text-dark: #2b2b2b;
    --white: #ffffff;
    --product-metal: #8f8f8f;
    --product-brass: #d9a53a;
  }
  * { margin: 0; padding: 0; box-sizing: border-box; }
  html, body { width: 1200px; height: 190px; overflow: hidden; }
  body { font-family: "Open Sans", Arial, sans-serif; }
  .banner {
    position: relative;
    width: 1200px;
    height: 190px;
    background: linear-gradient(180deg, var(--bg-top), var(--bg-bottom));
  }
  .brand-kicker {
    position: absolute;
    left: 48px;
    top: 30px;
    font-size: 31px;
    font-weight: 400;
    letter-spacing: 0.5px;
    color: var(--brand-red);
    line-height: 1;
    white-space: nowrap;
  }
  .brand-name {
    position: absolute;
    left: 45px;
    top: 62px;
    font-size: 84px;
    font-weight: 700;
    letter-spacing: -1px;
    color: var(--brand-brown);
    line-height: 1;
    white-space: nowrap;
  }
  .address {
    position: absolute;
    left: 48px;
    top: 151px;
    font-size: 22px;
    color: var(--text-dark);
    line-height: 1;
    white-space: nowrap;
  }
  .phone-box {
    position: absolute;
    left: 475px;
    top: 32px;
    width: 218px;
    height: 98px;
    background: var(--brand-red);
    display: flex;
    align-items: center;
    justify-content: center;
  }
  .phone-number {
    color: var(--white);
    font-size: 28px;
    font-weight: 700;
    letter-spacing: 0.3px;
    white-space: nowrap;
  }
  .product-photo {
    position: absolute;
    left: 776px;
    top: 8px;
    width: 332px;
    height: 160px;
    border-radius: 6px;
    background: radial-gradient(ellipse at 65% 40%, var(--product-metal), rgba(143,143,143,0) 70%),
                radial-gradient(ellipse at 30% 70%, var(--product-brass), rgba(217,165,58,0) 65%);
  }
</style>
</head>
<body>
  <div class="banner">
    <div class="brand-kicker">PINECREST VALLEY</div>
    <div class="brand-name">ARMORY</div>
    <div class="address">412 Route 19 South, Ridgeford Vy. 39417</div>
    <div class="phone-box"><span class="phone-number">555-574-3186</span></div>
    <div class="product-photo" role="img" aria-label="Photo of a semi-automatic pistol resting on a scattered pile of brass ammunition rounds"></div>
  </div>
</body>
</html>
```